Re-Design an adult education portal

I need support to re-design an adult education portal. Currently the customer has an incomplete website which should be prepared in a new format.
I have the idea how to realize, but I have no clue how to design it. The hard thing is to have a "beautiful" website with available logo and main color. I hope you can support me.

Name of Website: tovrenu (tovrenu.ch)
Content: adult eduction for adult in safety at work, mountain climbing, dog school. various courses in different areas. But on old webpage is hard to find the different possibilities.
main color: Ral 6011 (green) -> #6C7C59
logo: you see on top of website the logo (2 dogs and a mountain with a colour gradient).

new website: for new webpage I decided to have a navigation for each section of education. In the main area I would like to have some pictures to give an idea what content is behind. At the moment it looks terrible, so I decided to use you as support for me to make the webpage prettier :). And maybe you have an better idea how to make it great. -> current state of new web page: https://tovrenu.bask-om.ch/

Target Market(s)

adult eduction for adult in safety at work, mountain climbing, dog school

Number of Pages Required

1 page

Font styles to use
Serif
Sans Serif

Requirements
Must have
• As main color is set "Ral 6011" (green) -> #6C7C59

```html
<!DOCTYPE html>
<html lang="en">
<head>
<meta charset="utf-8">
<title>tovrenu – Training &amp; Course Partner</title>
<link rel="stylesheet" href="https://fonts.googleapis.com/css2?family=Montserrat:wght@500;600;700;800&family=Open+Sans:wght@400;600&display=swap">
<style>
:root{
  --green:#6C7C59;
  --green-dark:#56643f;
  --green-deep:#3e4833;
  --ink:#1f1f1f;
  --text:#555;
  --white:#fff;
  --footer:#1d1d1d;
  --line:#d9d9d9;
}
*{margin:0;padding:0;box-sizing:border-box}
html,body{width:1200px;height:3348px;overflow:hidden}
body{font-family:"Open Sans",Arial,sans-serif;color:var(--text);background:#fff;position:relative}
h1,h2,h3,.nav a,.btn,.brand{font-family:"Montserrat",Arial,sans-serif}
.abs{position:absolute}

/* hero */
.hero{position:absolute;left:0;top:0;width:1200px;height:600px;
  background:linear-gradient(180deg,#8fa37a 0%,#5f7446 45%,#3d4d2c 100%)}
.hero-photo{position:absolute;inset:0;
  background:radial-gradient(ellipse at 70% 60%,#b44b3a 0 6%,transparent 22%),
  radial-gradient(ellipse at 80% 35%,#a9b7c4 0,transparent 30%),
  linear-gradient(180deg,rgba(0,0,0,.05),rgba(0,0,0,.25))}
.brand-box{position:absolute;left:112px;top:0;width:228px;height:80px;background:rgba(255,255,255,.92);
  display:flex;align-items:center;gap:12px;padding-left:18px}
.brand-dot{width:26px;height:26px;border-radius:50%;background:var(--green)}
.brand{font-size:30px;font-weight:700;color:var(--green)}
.nav{position:absolute;right:120px;top:30px;display:flex;gap:40px}
.nav a{color:#fff;text-decoration:none;font-size:15px;font-weight:600;letter-spacing:.5px}
.hero h1{position:absolute;left:112px;top:212px;color:#fff;font-size:48px;line-height:52px;font-weight:800;text-transform:uppercase}
.hero p{position:absolute;left:112px;top:326px;width:430px;color:#fff;font-size:15px;line-height:22px;font-weight:600}
.btn{display:inline-block;font-size:15px;font-weight:600;border-radius:24px;text-align:center}
.hero .btn{position:absolute;left:112px;top:414px;width:184px;height:44px;line-height:42px;background:var(--green-dark);color:#fff;border:1px solid rgba(255,255,255,.6)}
.dots{position:absolute;left:560px;top:570px;display:flex;gap:10px}
.dots i{width:10px;height:10px;border-radius:50%;background:rgba(255,255,255,.6)}
.dots i:first-child{background:#fff}

/* section titles */
.section-title{position:absolute;left:0;width:1200px;text-align:center;color:var(--ink);font-size:40px;font-weight:700;text-transform:uppercase}

/* courses */
.course{position:absolute;top:752px;width:300px;height:404px;background:#fff;box-shadow:0 4px 16px rgba(0,0,0,.15);text-align:center}
.course .pic{height:204px}
.course h3{margin-top:20px;font-size:22px;font-weight:700;color:var(--ink);text-transform:uppercase}
.course p{margin:10px 22px 0;font-size:12px;line-height:18px;height:56px}
.course .btn{margin-top:22px;width:156px;height:40px;line-height:40px;background:var(--green);color:#fff;font-size:14px}
.arrow{position:absolute;top:940px}
.view-all{position:absolute;left:504px;top:1186px;width:192px;height:44px;line-height:42px;border:2px solid var(--green);color:var(--ink);font-size:14px}

/* about */
.about{position:absolute;left:0;top:1320px;width:1200px;height:432px;background:var(--green)}
.about .pic{position:absolute;left:120px;top:60px;width:250px;height:262px}
.about h2{position:absolute;left:652px;top:104px;color:#fff;font-size:40px;font-weight:700}
.about p{position:absolute;left:652px;top:168px;width:440px;color:#eef0ea;font-size:12.5px;line-height:21px}
.about .btn{position:absolute;left:652px;top:358px;width:168px;height:44px;line-height:40px;border:2px solid #fff;color:#fff}

/* dogs */
.dog{position:absolute;top:1960px;width:312px;height:380px}
.dog .pic{height:312px}
.dog .name{height:68px;line-height:68px;background:var(--green);color:#fff;text-align:center;font-family:"Montserrat",Arial,sans-serif;font-size:20px;font-weight:700}

/* contact */
.contact{position:absolute;left:0;top:2420px;width:1200px;height:560px;
  background:linear-gradient(160deg,#4b573f,#323b2a 70%,#2a3223)}
.contact h2{position:absolute;left:0;width:1200px;top:80px;text-align:center;color:#fff;font-size:40px;font-weight:700}
.field{position:absolute;height:44px;background:#fff;border:1px solid var(--line);padding:0 14px;line-height:42px;font-size:13px;color:#777}
.submit{position:absolute;left:504px;top:432px;width:124px;height:42px;line-height:38px;border:2px solid #fff;color:#fff;font-size:14px}

/* footer */
.footer{position:absolute;left:0;top:2980px;width:1200px;height:368px;background:var(--footer);color:#ccc}
.footer .brand-box{left:112px;top:60px;width:200px;height:100px;justify-content:center;padding:0}
.footer .brand{font-size:26px}
.social{position:absolute;left:144px;top:200px;display:flex;gap:10px}
.social i{width:28px;height:28px;border-radius:50%;background:#fff}
.footer h4{font-family:"Montserrat",Arial,sans-serif;font-size:15px;font-weight:700;color:#fff;text-transform:uppercase;margin-bottom:10px}
.footer h4::after{content:"";display:block;width:34px;height:2px;background:var(--green);margin-top:8px}
.col{position:absolute;top:56px;font-size:13px;line-height:26px}
.col a{display:block;color:#ccc;text-decoration:none}
.contact-line{display:flex;align-items:center;gap:10px;margin-bottom:8px}
.sub-text{width:240px;line-height:20px;margin-bottom:18px}
.sub-form{display:flex;width:250px;height:44px}
.sub-form span{flex:1;background:#fff;color:#888;line-height:44px;padding-left:12px}
.sub-form b{width:44px;background:var(--green);display:flex;align-items:center;justify-content:center}
.copy{position:absolute;left:0;top:3292px;width:1200px;text-align:center;font-size:12px;color:#ccc;border-top:1px solid #333;padding-top:18px}
</style>
</head>
<body>

<header class="hero">
  <div class="hero-photo" role="img" aria-label="Photo of a smiling couple with two brown hunting dogs in front of green mountains"></div>
  <div class="brand-box"><span class="brand-dot"></span><span class="brand">tovrenu.ch</span></div>
  <nav class="nav"><a href="#">HOME</a><a href="#">ABOUT</a><a href="#">OUR COURSE</a><a href="#">OUR DOG</a><a href="#">CONTACT US</a></nav>
  <h1>Your Training &amp;<br>Course Partner</h1>
  <p>We offer training tailored to your needs, target-oriented and tailored to your skills &amp; knowledge.</p>
  <a class="btn" href="#">Get Started</a>
  <div class="dots"><i></i><i></i><i></i></div>
</header>

<h2 class="section-title" style="top:680px">Our Courses</h2>
<svg class="arrow" style="left:76px" width="16" height="28" viewBox="0 0 16 28"><path d="M13 2 3 14l10 12" fill="none" stroke="#888" stroke-width="3"/></svg>
<svg class="arrow" style="left:1108px" width="16" height="28" viewBox="0 0 16 28"><path d="M3 2l10 12L3 26" fill="none" stroke="#888" stroke-width="3"/></svg>

<article class="course" style="left:120px">
  <div class="pic" role="img" aria-label="Photo of a fire engine and an accident warning sign" style="background:linear-gradient(135deg,#b83a2c,#8d8f94 60%,#dfe2e6)"></div>
  <h3>First Aiders</h3>
  <p>We have been working full-time or part-time in the emergency services since 1996. We run the emergency helper course for drivers license.</p>
  <a class="btn" href="#">LEARN MORE</a>
</article>
<article class="course" style="left:450px">
  <div class="pic" role="img" aria-label="Photo of rescue vehicles parked at a dog training ground" style="background:linear-gradient(135deg,#c04437,#6e7069 55%,#3b3d38)"></div>
  <h3>Dog School</h3>
  <p>At our dog park we mainly conduct puppy courses, team assessments, dog training and certification. If the situation allows</p>
  <a class="btn" href="#">LEARN MORE</a>
</article>
<article class="course" style="left:780px">
  <div class="pic" role="img" aria-label="Photo of a first aid resuscitation training" style="background:linear-gradient(135deg,#d9b7a0,#c08a6c 50%,#f0eeea)"></div>
  <h3>Rescue &amp; Medical</h3>
  <p>We offer you customized courses in the medical and rescue area according to your wishes. Company courses are adapted.</p>
  <a class="btn" href="#">LEARN MORE</a>
</article>
<a class="btn view-all" href="#">View All Courses</a>

<section class="about">
  <div class="pic" role="img" aria-label="Photo of the couple sitting on a mountain meadow with their three dogs" style="background:linear-gradient(160deg,#7f8d6a,#4e5a3a 55%,#6b5a44)"></div>
  <h2>ABOUT US</h2>
  <p>In my professional career, I have repeatedly experienced situations that gave me the idea of giving more information on practical knowledge that would allow them to react correctly and with the necessary calm in an emergency. The pooling and combining of knowledge and skills from the various specialist areas gives people security and confidence in their actions. Our own experience has shown that the more prepared you are the better you act.</p>
  <a class="btn" href="#">Learn More</a>
</section>

<h2 class="section-title" style="top:1892px">Our Dogs</h2>
<div class="dog" style="left:112px"><div class="pic" role="img" aria-label="Photo of the black and tan dog Akila on grass" style="background:linear-gradient(160deg,#9fae7e,#3a3128 55%,#6d8a4a)"></div><div class="name">AKILA</div></div>
<div class="dog" style="left:444px"><div class="pic" role="img" aria-label="Photo of the brown dog Jil lying in the garden" style="background:linear-gradient(160deg,#8da06c,#8a4a28 55%,#5d7a3c)"></div><div class="name">JIL</div></div>
<div class="dog" style="left:776px"><div class="pic" role="img" aria-label="Photo of the brown and white dog Heimo lying on grass" style="background:linear-gradient(160deg,#a7b68d,#4a3226 50%,#e6e3dd 70%,#6f8c4e)"></div><div class="name">HEIMO</div></div>

<section class="contact">
  <h2>CONTACT US</h2>
  <div class="field" style="left:320px;top:150px;width:268px">First Name</div>
  <div class="field" style="left:604px;top:150px;width:272px">Last Name</div>
  <div class="field" style="left:320px;top:208px;width:556px">Email Address</div>
  <div class="field" style="left:320px;top:266px;width:268px">City</div>
  <div class="field" style="left:604px;top:266px;width:272px">Phone Number</div>
  <div class="field" style="left:320px;top:324px;width:556px;height:88px">Message</div>
  <a class="btn submit" href="#">SUBMIT</a>
</section>

<footer class="footer">
  <div class="brand-box"><span class="brand-dot"></span><span class="brand">tovrenu.ch</span></div>
  <div class="social"><i></i><i></i><i></i><i></i></div>
  <div class="col" style="left:392px"><h4>Quick Links</h4><a href="#">Home</a><a href="#">About</a><a href="#">Our course</a><a href="#">Our dog</a><a href="#">Contact us</a></div>
  <div class="col" style="left:572px"><h4>Contact Us</h4>
    <div class="contact-line"><svg width="14" height="18" viewBox="0 0 14 18"><path d="M7 1a6 6 0 0 0-6 6c0 4.5 6 10 6 10s6-5.5 6-10a6 6 0 0 0-6-6z" fill="var(--green)"/><circle cx="7" cy="7" r="2.2" fill="#1d1d1d"/></svg><span>Lindenweg 14<br>8907 Felsbach</span></div>
    <div class="contact-line"><svg width="16" height="16" viewBox="0 0 16 16"><path d="M3 1h3l1.5 4-2 1.3a9 9 0 0 0 4.2 4.2L11 8.5l4 1.5v3a2 2 0 0 1-2 2A12 12 0 0 1 1 3a2 2 0 0 1 2-2z" fill="var(--green)"/></svg><span>+41 79 000 12 34</span></div>
    <div class="contact-line"><svg width="16" height="12" viewBox="0 0 16 12"><rect width="16" height="12" rx="1" fill="var(--green)"/><path d="M1 1l7 6 7-6" fill="none" stroke="#1d1d1d" stroke-width="1.4"/></svg><span>info@tovrenu.ch</span></div>
  </div>
  <div class="col" style="left:820px"><h4>Subscribe to our blog</h4>
    <p class="sub-text">Sign up today to get resources on how to attract and retain more customers!</p>
    <div class="sub-form"><span>Email Address</span><b><svg width="18" height="16" viewBox="0 0 18 16"><path d="M1 8l16-7-4 14-4-5-8-2z" fill="#fff"/></svg></b></div>
  </div>
  <p class="copy">Copyright © 2021 TOVRENU Reserved</p>
</footer>

</body>
</html>
```